New Product Design

We want to develop new Wafer Biscuits Product design of Vanilla / strawberry / choclate flavour. Designer can design first any of the flavour ( Vanilla/Chcolate/Starwberry). Based on the first any variety design will go for other designs.
Wafer is in finger form .
Name of the Brand will be TOBI LUN
Wafer fingre (sample pics and TOBI LUN brand image is attached in word file for reference.

Smaple pics of the fingre is attached for ref.

Target Market(s)

Children and Youth

Industry/Entity Type

Food

```html
<!DOCTYPE html>
<html lang="en">
<head>
<meta charset="utf-8">
<title>TOBI LUN Wafer Biscuits – Vanilla Flavoured Pack</title>
<link rel="stylesheet" href="https://fonts.googleapis.com/css2?family=Fredoka:wght@500;600;700&family=Questrial&display=swap">
<style>
  :root {
    --backdrop: #d873b2;
    --magenta: #b5127a;
    --magenta-deep: #8e0c5f;
    --magenta-light: #d8529f;
    --white: #ffffff;
    --band-white: #f4f1f3;
    --ink-grey: #6a4a5c;
    --wafer-cream: #e8d4b4;
    --wafer-filling: #a5607e;
    --berry-red: #d94a56;
    --leaf-green: #6ea84a;
  }
  * { margin: 0; padding: 0; box-sizing: border-box; }
  html, body { width: 1200px; height: 800px; overflow: hidden; }
  body {
    background: var(--backdrop);
    position: relative;
    font-family: "Fredoka", sans-serif;
  }
  .pack {
    position: absolute;
    left: 150px; top: 220px;
    width: 900px; height: 360px;
  }
  .pack-body {
    position: absolute;
    left: 60px; right: 60px; top: 0; bottom: 0;
    background: var(--magenta);
    overflow: hidden;
  }
  .white-band {
    position: absolute;
    left: 0; right: 0; top: 178px; height: 140px;
    background: var(--band-white);
    border-top: 4px solid var(--magenta-deep);
  }
  .bottom-stripe {
    position: absolute;
    left: 0; right: 0; bottom: 0; height: 42px;
    background: var(--magenta-deep);
  }
  .seal { position: absolute; top: 0; width: 60px; height: 360px; }
  .seal-left { left: 0; }
  .seal-right { right: 0; }
  .flavour-ribbon {
    position: absolute;
    left: 90px; top: 58px;
    width: 320px; height: 44px;
  }
  .flavour-ribbon svg { position: absolute; inset: 0; }
  .flavour-label {
    position: absolute; inset: 0;
    display: flex; align-items: center; justify-content: center;
    color: var(--band-white);
    font-weight: 600; font-size: 26px;
    letter-spacing: 0.5px;
  }
  .brand-name {
    position: absolute;
    left: 50px; top: 108px;
    color: var(--white);
    font-weight: 700; font-size: 80px;
    line-height: 1;
    letter-spacing: 1px;
    white-space: nowrap;
  }
  .product-name {
    position: absolute;
    left: 140px; top: 200px;
    color: var(--magenta);
    font-weight: 700; font-size: 44px;
    line-height: 1;
    white-space: nowrap;
  }
  .tagline {
    position: absolute;
    left: 168px; top: 258px;
    color: var(--ink-grey);
    font-family: "Questrial", sans-serif;
    font-size: 14px;
    white-space: nowrap;
  }
  .berry-photo {
    position: absolute;
    left: 20px; top: 200px;
    width: 78px; height: 72px;
    border-radius: 40%;
    background: radial-gradient(circle at 45% 55%, var(--berry-red), #e98a8f 60%, var(--leaf-green) 95%);
  }
  .wafer-photo {
    position: absolute;
    left: 490px; top: 100px;
    width: 270px; height: 150px;
    background: linear-gradient(160deg, var(--wafer-cream) 0%, var(--wafer-cream) 45%, var(--wafer-filling) 70%, var(--wafer-cream) 100%);
    border-radius: 10px;
    transform: skewY(10deg);
  }
</style>
</head>
<body>
  <div class="pack">
    <svg class="seal seal-left" viewBox="0 0 60 360" aria-hidden="true">
      <path d="M60 0 H14 l-8 10 8 10 -8 10 8 10 -8 10 8 10 -8 10 8 10 -8 10 8 10 -8 10 8 10 -8 10 8 10 -8 10 8 10 -8 10 8 10 -8 10 8 10 -8 10 8 10 -8 10 8 10 -8 10 8 10 -8 10 8 10 -8 10 8 10 -8 10 8 10 -8 10 8 10 -8 10 8 10 -8 10 8 10 V360 H60 Z" fill="#c7288c"/>
      <path d="M28 0 V360 M36 0 V360 M44 0 V360" stroke="#e37fbd" stroke-width="2"/>
    </svg>
    <div class="pack-body">
      <div class="white-band"></div>
      <div class="bottom-stripe"></div>
      <div class="berry-photo" role="img" aria-label="Photo of fresh strawberries with leaves"></div>
      <div class="wafer-photo" role="img" aria-label="Photo of wafer fingers with strawberry cream layers"></div>
      <div class="flavour-ribbon">
        <svg viewBox="0 0 320 44" aria-hidden="true">
          <path d="M0 8 H24 V36 H0 L10 22 Z M320 8 H296 V36 H320 L310 22 Z" fill="none" stroke="#f2c6df" stroke-width="2"/>
          <rect x="24" y="2" width="272" height="40" fill="var(--magenta-light)" stroke="#f2c6df" stroke-width="2"/>
        </svg>
        <div class="flavour-label">Vanilla Flavoured</div>
      </div>
      <div class="brand-name">TOBI LUN</div>
      <div class="product-name">Wafer Biscuits</div>
      <div class="tagline">Crispy wafer with Strawberry Cream Filling</div>
    </div>
    <svg class="seal seal-right" viewBox="0 0 60 360" aria-hidden="true">
      <path d="M0 0 H46 l8 10 -8 10 8 10 -8 10 8 10 -8 10 8 10 -8 10 8 10 -8 10 8 10 -8 10 8 10 -8 10 8 10 -8 10 8 10 -8 10 8 10 -8 10 8 10 -8 10 8 10 -8 10 8 10 -8 10 8 10 -8 10 8 10 -8 10 8 10 -8 10 8 10 -8 10 8 10 -8 10 8 10 -8 10 8 10 -8 10 8 10 -8 10 V360 H0 Z" fill="#c7288c"/>
      <path d="M16 0 V360 M24 0 V360 M32 0 V360" stroke="#e37fbd" stroke-width="2"/>
    </svg>
  </div>
</body>
</html>
```